PBG Business Card
Pelloway Building Group
PBG Business Card -
Creative Brief
Professional
Milo Pelloway
2274 Fenwick Avenue Shreveport, LA 71101
mpelloway@PellowayBG.com
PellowayBG.com
Logo and contact info on front. Logo to take up most of front of card with contact info in smaller text.
Pelloway Building Group (Notes) I would like a light grey color on the back with a navy border

```html
<!DOCTYPE html>
<html lang="en">
<head>
<meta charset="utf-8">
<title>Pelloway Building Group – Stationery</title>
<link href="https://fonts.googleapis.com/css2?family=Montserrat:wght@400;600;700&display=swap" rel="stylesheet">
<style>
  :root{
    --navy:#1f3f72;
    --sky:#7fa3cf;
    --paper:#ffffff;
    --grey:#d9dbde;
    --grey-dark:#9fa3a8;
    --ink:#3e434a;
    --faint:#e3e7ec;
    --backdrop:#e8e5e1;
  }
  *{box-sizing:border-box;margin:0;padding:0}
  html,body{width:1200px;height:341px;overflow:hidden}
  body{background:var(--backdrop);font-family:"Montserrat",sans-serif;position:relative;color:var(--ink)}
  .piece{position:absolute;overflow:hidden;box-shadow:0 2px 5px rgba(0,0,0,.18)}
  .wordmark{font-weight:700;color:var(--navy);letter-spacing:1px;line-height:1}
  .tagline{font-weight:600;color:var(--navy);font-size:5px;letter-spacing:.2px;margin-top:2px;white-space:nowrap}
  .tiny{font-size:5px;line-height:6.5px;color:var(--ink);white-space:nowrap}
  .wave{position:absolute;left:0;bottom:0;width:100%}

  /* business cards */
  .card{width:132px;height:77px;left:24px;border-radius:2px}
  .card-front{top:26px;background:var(--paper)}
  .card-front .brand{position:absolute;left:8px;top:8px}
  .card-front .wordmark{font-size:15px}
  .card-front .contact{position:absolute;left:8px;top:34px}
  .card-front .contact strong{font-size:5.5px;color:var(--navy);font-weight:700}
  .card-front .contact-right{position:absolute;right:6px;top:32px;text-align:right}
  .card-back-grey{top:122px;background:var(--grey);border:4px solid var(--navy)}
  .card-back-grey .inner{position:absolute;left:10px;right:10px;top:6px;height:22px;background:var(--paper);border-radius:2px;display:flex;align-items:center;justify-content:center}
  .card-back-grey .wordmark{font-size:12px}
  .card-back-grey .lines{position:absolute;left:14px;right:14px;top:36px}
  .card-back-grey .lines span{display:block;height:2px;background:var(--grey-dark);margin-bottom:5px;opacity:.6}
  .card-back-navy{top:221px;background:var(--navy)}
  .card-back-navy .plate{position:absolute;left:8px;top:12px;background:var(--paper);padding:3px 5px}
  .card-back-navy .wordmark{font-size:18px}

  /* letterheads */
  .letterhead{top:22px;width:216px;height:290px;background:var(--paper)}
  .lh-1{left:175px}
  .lh-2{left:408px}
  .letterhead .brand{position:absolute;left:50%;transform:translateX(-50%);top:12px;text-align:center}
  .letterhead .wordmark{font-size:14px}
  .lh-1 .brand{left:14px;transform:none;text-align:left}
  .lh-1 .head-contact{position:absolute;right:14px;top:12px;text-align:right}
  .letterhead .rule{position:absolute;left:14px;right:14px;top:42px;height:1px;background:var(--sky)}
  .letterhead .ghost{position:absolute;left:0;right:0;top:110px;text-align:center;font-weight:700;font-size:44px;color:var(--faint);letter-spacing:3px}
  .letterhead .footer{position:absolute;left:0;right:0;bottom:5px;text-align:center;color:#fff;font-size:4.5px;white-space:nowrap}

  /* small envelopes */
  .envelope{width:214px;height:98px;left:643px;background:var(--paper)}
  .env-1{top:82px}
  .env-2{top:204px}
  .envelope .brand{position:absolute;left:10px;top:8px}
  .envelope .wordmark{font-size:11px}
  .envelope .ghost{position:absolute;left:0;right:0;top:32px;text-align:center;font-weight:700;font-size:28px;color:var(--faint);letter-spacing:2px}

  /* long envelopes */
  .long{width:246px;height:92px;left:920px}
  .long-grey{top:22px;background:var(--grey)}
  .long-navy{top:120px;background:var(--paper)}
  .long-white{top:220px;background:var(--paper)}
  .long svg.flap{position:absolute;inset:0;width:100%;height:100%}
  .long .return{position:absolute;left:50%;transform:translateX(-50%);text-align:center}
  .long-navy .return{top:56px}
  .long-white .return{top:48px}
  .long .return .wordmark{font-size:6px;letter-spacing:.5px}
</style>
</head>
<body>

<div class="piece card card-front">
  <div class="brand">
    <div class="wordmark">PBG</div>
    <div class="tagline">PELLOWAY BUILDING GROUP</div>
  </div>
  <div class="contact tiny">
    <strong>Milo Pelloway</strong><br>Owner
  </div>
  <div class="contact-right tiny">
    (318) 555-0142<br>mpelloway@PellowayBG.com<br>2274 Fenwick Avenue<br>Shreveport, LA 71101
  </div>
  <svg class="wave" viewBox="0 0 132 16" preserveAspectRatio="none" aria-hidden="true">
    <path d="M0 10 C40 2 80 14 132 5 L132 16 L0 16Z" fill="var(--navy)"/>
    <path d="M0 7 C40 0 80 11 132 2" fill="none" stroke="var(--sky)" stroke-width=".8"/>
  </svg>
</div>

<div class="piece card card-back-grey">
  <div class="inner"><span class="wordmark">PBG</span></div>
  <div class="lines"><span></span><span></span><span></span></div>
</div>

<div class="piece card card-back-navy">
  <div class="plate"><span class="wordmark">PBG</span></div>
  <svg class="wave" viewBox="0 0 132 20" preserveAspectRatio="none" aria-hidden="true">
    <path d="M0 14 C40 4 80 20 132 8" fill="none" stroke="var(--sky)" stroke-width=".8"/>
  </svg>
</div>

<div class="piece letterhead lh-1">
  <div class="brand">
    <div class="wordmark">PBG</div>
    <div class="tagline">PELLOWAY BUILDING GROUP</div>
  </div>
  <div class="head-contact tiny">2274 Fenwick Avenue<br>Shreveport, LA 71101<br>(318) 555-0142<br>PellowayBG.com</div>
  <div class="rule"></div>
  <div class="ghost">PBG</div>
  <svg class="wave" viewBox="0 0 216 30" preserveAspectRatio="none" aria-hidden="true">
    <path d="M0 18 C70 4 140 26 216 10 L216 30 L0 30Z" fill="var(--navy)"/>
    <path d="M0 14 C70 0 140 22 216 6" fill="none" stroke="var(--sky)" stroke-width="1"/>
  </svg>
  <div class="footer">2274 Fenwick Avenue · Shreveport, LA 71101 · PellowayBG.com</div>
</div>

<div class="piece letterhead lh-2">
  <div class="brand">
    <div class="wordmark">PBG</div>
    <div class="tagline">PELLOWAY BUILDING GROUP</div>
  </div>
  <div class="rule"></div>
  <div class="ghost">PBG</div>
  <svg class="wave" viewBox="0 0 216 30" preserveAspectRatio="none" aria-hidden="true">
    <path d="M0 18 C70 4 140 26 216 10 L216 30 L0 30Z" fill="var(--navy)"/>
    <path d="M0 14 C70 0 140 22 216 6" fill="none" stroke="var(--sky)" stroke-width="1"/>
  </svg>
  <div class="footer">2274 Fenwick Avenue · Shreveport, LA 71101 · PellowayBG.com</div>
</div>

<div class="piece envelope env-1">
  <div class="brand">
    <div class="wordmark">PBG</div>
    <div class="tagline">PELLOWAY BUILDING GROUP</div>
  </div>
  <div class="ghost">PBG</div>
  <svg class="wave" viewBox="0 0 214 20" preserveAspectRatio="none" aria-hidden="true">
    <path d="M0 12 C70 2 140 18 214 6 L214 20 L0 20Z" fill="var(--navy)"/>
    <path d="M0 9 C70 0 140 15 214 3" fill="none" stroke="var(--sky)" stroke-width=".8"/>
  </svg>
</div>
<div class="piece envelope env-2">
  <div class="brand">
    <div class="wordmark">PBG</div>
    <div class="tagline">PELLOWAY BUILDING GROUP</div>
  </div>
  <div class="ghost">PBG</div>
  <svg class="wave" viewBox="0 0 214 20" preserveAspectRatio="none" aria-hidden="true">
    <path d="M0 12 C70 2 140 18 214 6 L214 20 L0 20Z" fill="var(--navy)"/>
    <path d="M0 9 C70 0 140 15 214 3" fill="none" stroke="var(--sky)" stroke-width=".8"/>
  </svg>
</div>

<div class="piece long long-grey">
  <svg class="flap" viewBox="0 0 246 92" preserveAspectRatio="none" aria-hidden="true">
    <path d="M0 0 L123 34 L246 0Z" fill="#c6c9cd"/>
    <path d="M0 92 L110 46 M246 92 L136 46" stroke="#c0c3c7" stroke-width="1" fill="none"/>
  </svg>
</div>
<div class="piece long long-navy">
  <svg class="flap" viewBox="0 0 246 92" preserveAspectRatio="none" aria-hidden="true">
    <path d="M0 0 L246 0 L246 8 C180 40 66 40 0 8Z" fill="var(--navy)"/>
    <path d="M0 92 L100 50 M246 92 L146 50" stroke="#e6e8eb" stroke-width="1" fill="none"/>
  </svg>
  <div class="return"><div class="wordmark">PBG</div></div>
</div>
<div class="piece long long-white">
  <svg class="flap" viewBox="0 0 246 92" preserveAspectRatio="none" aria-hidden="true">
    <path d="M0 0 L123 40 L246 0" stroke="#e3e5e8" stroke-width="1" fill="none"/>
    <path d="M0 92 L100 50 M246 92 L146 50" stroke="#e6e8eb" stroke-width="1" fill="none"/>
  </svg>
  <div class="return"><div class="wordmark">PBG</div></div>
</div>

</body>
</html>
```